Sales sheet for printing and embroidery apparel items - Copper Fern Prints

I would like a one page flyer or sales sheet that I would use as a template to send different images of apparel we produce. I have attached examples of layouts I like.
- Ideally, it would have space for 3-5 items.
- I would like it one page only - not a folding flyer.
- Our companies name is Copper Fern Prints.
- This will be used for many different products and markets so I don't need wording/copy. You can use wording from the 7Q7 or K81 flyer.

Colors
0054AA
0677BA
7BADD7
CADEEF
E8F1F8
00AB8E
00BBA5
67D7C9
C6EFE9
E9F9F6
FFC000
F8CF3A
FAE287
FDF2CF
FEFAEE

Requirements
Must have
• Places for between 3 and 5 images of apparel (t-shirts, hats etc)

```html
<!DOCTYPE html>
<html lang="en">
<head>
<meta charset="UTF-8">
<title>Copper Fern Prints – Sales Sheet</title>
<link rel="stylesheet" href="https://fonts.googleapis.com/css2?family=Montserrat:wght@400;500;600;700;800&family=Oswald:wght@700&display=swap">
<style>
  :root {
    --navy: #173d6e;
    --ink: #1b3a6b;
    --orange: #e2622f;
    --paper: #ffffff;
    --backdrop: #bdbec0;
    --edge: #cfd0d2;
  }
  * { box-sizing: border-box; margin: 0; padding: 0; }
  html, body { width: 1200px; height: 1200px; overflow: hidden; }
  body { background: var(--backdrop); font-family: "Montserrat", Arial, sans-serif; color: var(--ink); }

  .sheet {
    position: absolute; left: 175px; top: 0;
    width: 849px; height: 1200px;
    background: var(--paper);
    overflow: hidden;
  }
  .hero-band { position: absolute; left: 0; top: 0; width: 849px; height: 640px; }

  .hero-products {
    position: absolute; left: 337px; top: 200px; width: 512px; height: 400px;
    background: radial-gradient(ellipse at 45% 50%, #1d2a4f 0%, #243258 45%, rgba(210,208,204,0.9) 80%, rgba(23,61,110,0) 100%);
    border-radius: 40% 10% 0 30%;
  }

  .brand { position: absolute; left: 640px; top: 54px; width: 190px; text-align: center; z-index: 2; }
  .brand-square { width: 100px; height: 76px; margin: 0 auto 14px; background: var(--orange); border: 3px solid var(--navy); }
  .brand-name { font-weight: 800; font-size: 15px; line-height: 1.1; color: #fff; text-transform: uppercase; white-space: nowrap; }

  .headline { position: absolute; left: 41px; top: 160px; font-family: "Oswald", Impact, sans-serif; font-weight: 700; text-transform: uppercase; }
  .headline .lead { display: block; color: #fff; font-size: 77px; line-height: 70px; }
  .headline .sub { display: block; color: var(--orange); font-size: 51px; line-height: 49px; }
  .headline .lead + .sub { margin-top: 10px; }

  .intro { position: absolute; left: 41px; top: 440px; color: #fff; font-size: 15px; line-height: 19.5px; white-space: nowrap; }

  .order-badge { position: absolute; left: 578px; top: 538px; width: 204px; height: 158px; z-index: 2; }
  .order-badge svg { position: absolute; inset: 0; }
  .order-badge .label {
    position: absolute; inset: 0; display: flex; align-items: center; justify-content: center;
    color: #fff; font-weight: 800; font-size: 31px; line-height: 30px; text-align: center;
    transform: rotate(-8deg);
  }

  .section-kicker { position: absolute; left: 41px; top: 650px; font-size: 20px; font-weight: 500; text-transform: uppercase; }
  .section-title { position: absolute; left: 39px; top: 674px; font-size: 41px; font-weight: 800; text-transform: uppercase; letter-spacing: 0.3px; }

  .product { position: absolute; top: 739px; width: 180px; }
  .product-frame { height: 159px; padding: 4px; background: #fff; box-shadow: 0 1px 4px rgba(0,0,0,0.35); }
  .product-photo { width: 100%; height: 100%; }
  .product-name { margin-top: 18px; text-align: center; font-size: 13px; font-weight: 500; text-transform: uppercase; white-space: nowrap; }
  .photo-hoodie { background: linear-gradient(#d9d9d9, #1a1a1a 40%, #111); }
  .photo-cap { background: linear-gradient(#e4e4e4, #1b1b1b 45%, #141414); }
  .photo-tee { background: linear-gradient(#d6d8dc, #1c2d5a 35%, #1a2a55); }
  .photo-patch { background: radial-gradient(circle, #5bb84d, #2a2a2a 60%, #e8e8e8 92%); }

  .feature { position: absolute; top: 960px; }
  .feature-icon { position: absolute; left: 0; top: 0; width: 50px; height: 50px; border-radius: 50%; background: var(--orange); display: flex; align-items: center; justify-content: center; }
  .feature-text { position: absolute; left: 63px; top: 8px; width: 220px; }
  .feature-title { font-size: 22px; font-weight: 700; line-height: 19px; }
  .feature-desc { margin-top: 12px; font-size: 14px; line-height: 17px; white-space: nowrap; }

  .footer-rule { position: absolute; left: 45px; top: 1082px; width: 756px; height: 1.5px; background: var(--ink); }
  .footer-divider { position: absolute; top: 1095px; width: 1.5px; height: 56px; background: var(--ink); }
  .phone-label { position: absolute; left: 50px; top: 1096px; font-size: 24px; font-weight: 700; }
  .phone-number { position: absolute; left: 45px; top: 1122px; font-size: 27px; font-weight: 700; }
  .contact-icon { position: absolute; }
  .contact-text { position: absolute; font-size: 14px; line-height: 18px; white-space: nowrap; }
</style>
</head>
<body>
<main class="sheet">

  <svg class="hero-band" viewBox="0 0 849 640" aria-hidden="true">
    <path d="M0 112 C60 96 100 72 160 73 C240 74 300 96 380 92 C470 88 560 64 640 74 C690 80 720 112 760 112 C800 112 820 100 849 97 L849 578 C760 582 640 596 562 596 C510 596 480 610 450 608 C420 606 400 588 375 589 C300 590 230 606 165 604 C100 602 50 570 0 566 Z" fill="var(--edge)"/>
    <path d="M0 116 C60 100 100 76 160 77 C240 78 300 100 380 96 C470 92 560 68 640 78 C690 84 720 116 760 116 C800 116 820 104 849 101 L849 574 C760 578 640 592 562 592 C510 592 480 606 450 604 C420 602 400 584 375 585 C300 586 230 602 165 600 C100 598 50 566 0 562 Z" fill="var(--navy)"/>
  </svg>

  <div class="hero-products" role="img" aria-label="Featured apparel: navy printed hoodie, embroidered trucker cap and light printed t-shirt"></div>

  <div class="brand">
    <div class="brand-square"></div>
    <div class="brand-name">Copper Fern Prints</div>
  </div>

  <h1 class="headline">
    <span class="lead">Custom</span>
    <span class="lead">Apparel</span>
    <span class="sub">Printing &amp;</span>
    <span class="sub">Embroidery</span>
  </h1>

  <p class="intro">Custom shirts, hats, patches<br>and branded merchandise<br>for schools, teams, churches,<br>businesses and events.</p>

  <div class="order-badge">
    <svg viewBox="0 0 204 158" aria-hidden="true">
      <ellipse cx="102" cy="79" rx="101" ry="77" fill="var(--edge)" transform="rotate(-8 102 79)"/>
      <ellipse cx="102" cy="77" rx="98" ry="74" fill="var(--orange)" transform="rotate(-8 102 77)"/>
    </svg>
    <div class="label">START<br>YOUR<br>ORDER</div>
  </div>

  <p class="section-kicker">Your brand deserves</p>
  <h2 class="section-title">The best apparel</h2>

  <figure class="product" style="left:37px">
    <div class="product-frame"><div class="product-photo photo-hoodie" role="img" aria-label="Black hoodie with embroidered chest design"></div></div>
    <figcaption class="product-name">Premium Embroidery</figcaption>
  </figure>
  <figure class="product" style="left:231px">
    <div class="product-frame"><div class="product-photo photo-cap" role="img" aria-label="Black cap with raised embroidered lettering"></div></div>
    <figcaption class="product-name">Custom Headwear</figcaption>
  </figure>
  <figure class="product" style="left:426px">
    <div class="product-frame"><div class="product-photo photo-tee" role="img" aria-label="Navy t-shirt with screen printed graphic"></div></div>
    <figcaption class="product-name">Screen Printed Tees</figcaption>
  </figure>
  <figure class="product" style="left:621px">
    <div class="product-frame"><div class="product-photo photo-patch" role="img" aria-label="Colourful printed patch on black backing"></div></div>
    <figcaption class="product-name">Patches &amp; Transfers</figcaption>
  </figure>

  <div class="feature" style="left:40px">
    <div class="feature-icon">
      <svg width="28" height="28" viewBox="0 0 28 28" fill="none" stroke="#fff" stroke-width="1.6"><path d="M4 9 L14 4 L24 9 L24 20 L14 25 L4 20 Z M4 9 L14 14 L24 9 M14 14 L14 25 M9 6.5 L19 11.5"/></svg>
    </div>
    <div class="feature-text">
      <div class="feature-title">No<br>Inventory</div>
      <p class="feature-desc">We produce what you<br>need, when you need it.</p>
    </div>
  </div>
  <div class="feature" style="left:293px">
    <div class="feature-icon">
      <svg width="28" height="28" viewBox="0 0 28 28" fill="none" stroke="#fff" stroke-width="1.6"><rect x="5" y="6" width="18" height="12" rx="1"/><path d="M3 21 H25 M11 18 V21 M17 18 V21"/></svg>
    </div>
    <div class="feature-text">
      <div class="feature-title">Online<br>Stores</div>
      <p class="feature-desc">Branded merch stores for<br>teams, schools, and shops.</p>
    </div>
  </div>
  <div class="feature" style="left:553px">
    <div class="feature-icon">
      <svg width="30" height="28" viewBox="0 0 30 28" fill="none" stroke="#fff" stroke-width="1.6"><path d="M3 8 H18 V20 H3 Z M18 12 H23 L27 16 V20 H18"/><circle cx="8" cy="21" r="2.2" fill="var(--orange)"/><circle cx="22" cy="21" r="2.2" fill="var(--orange)"/></svg>
    </div>
    <div class="feature-text">
      <div class="feature-title">Direct<br>Shipping</div>
      <p class="feature-desc">We pack and ship orders<br>straight to your destination.</p>
    </div>
  </div>

  <div class="footer-rule"></div>
  <p class="phone-label">Phone info</p>
  <p class="phone-number">+1 555-418-2730</p>

  <div class="footer-divider" style="left:308px"></div>
  <svg class="contact-icon" style="left:330px; top:1108px" width="22" height="30" viewBox="0 0 22 30" fill="none" stroke="var(--ink)" stroke-width="1.6"><path d="M11 28 C11 28 2 17 2 11 A9 9 0 0 1 20 11 C20 17 11 28 11 28 Z"/><circle cx="11" cy="11" r="3.5"/></svg>
  <p class="contact-text" style="left:360px; top:1104px">845 Fernwood Lane<br>Maple Hollow, OR 97999</p>

  <div class="footer-divider" style="left:564px"></div>
  <svg class="contact-icon" style="left:590px; top:1113px" width="28" height="20" viewBox="0 0 28 20" fill="none" stroke="var(--ink)" stroke-width="1.6"><rect x="1" y="1" width="26" height="18"/><path d="M1 1 L14 11 L27 1 M1 19 L11 9 M27 19 L17 9"/></svg>
  <p class="contact-text" style="left:626px; top:1104px">info@copperfernprints.com<br>www.copperfernprints.com</p>

</main>
</body>
</html>
```